Redesign Call Answering Service Company Website

There is a good explanation of what we do at existing website hummingdesk.com.au.

We are getting traffic and now want to increase conversions and reduce drop offs. We need to create trust very quickly.

Once website done we will be looking to redesign logo.

We want to use “F” shaped reading pattern for website viewers. 2 very rough ideas on attached wireframes docs. The winning site only needs to follow the rough layout – no need for boxes, etc. Looking for creative help here!

One page needed (home page) that easily becomes all other pages without a "price reference" (see wire frames).

All existing pages will have new/updated content added with extra pages added.

Target Market(s)

Target market to appeal to is 70% females 25 to 60, self-employed business owners, complimentary/alternative therapists, small to medium business ente

Industry/Entity Type

It Company

Requirements
Must have
• must have items on wire frames
must have a Client Login (to self-service area)
must have a Contact Area with 4 x phone numbers, 1 x fax number and email/contact us

```html
<!DOCTYPE html>
<html lang="en">
<head>
<meta charset="utf-8">
<title>Humming Desk – Call Answering</title>
<link href="https://fonts.googleapis.com/css2?family=Arimo:wght@400;700&display=swap" rel="stylesheet">
<style>
:root{
  --sky:#35abd9;--sky-light:#8fd3ee;--sky-deep:#1f8fc4;
  --ink:#4d7c90;--ink-dark:#3c6475;--text-blue:#5a93aa;--news-grey:#6d97a8;
  --green:#9fe01c;--green-light:#c3f03a;--green-dark:#86c612;
  --white:#fff;--grey-line:#d9dde0;--nav-grey:#efefef;
}
*{margin:0;padding:0;box-sizing:border-box}
html,body{width:1200px;height:1178px;overflow:hidden;background:#fff;font-family:"Arimo",Helvetica,Arial,sans-serif}
.page{position:relative;width:1200px;height:1178px;overflow:hidden}
.abs{position:absolute}
.header{left:0;top:0;width:1200px;height:150px;background:linear-gradient(100deg,#8fd0ec 0%,#4fb6e0 45%,#2ea6d8 100%)}
.brand{display:flex;align-items:center;gap:10px;color:#fff;font-weight:700;font-size:27px;line-height:28px;text-transform:uppercase}
.brand-mark{width:44px;height:44px;background:#fff;border-radius:6px;flex:none}
.tagline{left:459px;top:46px;color:#fff;font-size:25px;line-height:29px}
.tagline span{display:block;font-size:24px;opacity:.95}
.login{left:953px;top:52px;width:108px;height:38px;background:#fff;border-radius:5px;display:flex;align-items:center;gap:10px;padding-left:13px;color:var(--text-blue);font-size:16px}
.nav{left:141px;top:130px;width:925px;height:47px;background:linear-gradient(#fff,#ececec);border-radius:4px;box-shadow:0 6px 10px rgba(0,0,0,.08);display:flex}
.nav a{display:flex;align-items:center;padding:0 16px;color:var(--text-blue);font-size:17px;text-decoration:none;border-right:1px solid #d6d6d6}
.nav a.active{background:linear-gradient(#47b3ea,#1f8fd4);color:#fff;border-top:3px solid var(--green);border-radius:4px 0 0 4px;gap:8px;width:94px;padding:0 10px}
.nav a.active svg{flex:none}
.nav a:last-child{border-right:none}
.photo{left:110px;top:220px;width:342px;height:233px;background:radial-gradient(circle at 55% 45%,#c9a38f 0%,#e9dcd4 35%,#f6f3f1 70%,#fff 100%)}
.features{left:332px;top:206px;list-style:none;color:var(--text-blue);font-size:13.5px;line-height:28px;width:495px;white-space:nowrap}
.features li{position:relative;padding-left:20px}
.features li::before,.links li::before{content:"";position:absolute;left:0;top:11px;border-left:5px solid var(--sky);border-top:3.5px solid transparent;border-bottom:3.5px solid transparent}
.price{left:825px;top:196px;width:241px;height:208px;border-radius:9px;background:linear-gradient(var(--green-light),var(--green));overflow:hidden;text-align:center;color:#fff}
.price .from{margin-top:12px;font-size:22px}
.price .amount{font-size:38px;font-weight:700;line-height:44px}
.price .amount small{font-size:22px;font-weight:400}
.trial{margin:9px auto 0;width:205px;height:45px;background:linear-gradient(#fff,#e5e5e5);border-radius:5px;color:#5c94a8;font-weight:700;font-size:22px;line-height:45px}
.plans{position:absolute;left:0;bottom:0;width:100%;height:50px;background:linear-gradient(#98d81c,#86c612);font-weight:700;font-size:22px;line-height:50px;text-align:left;padding-left:34px}
.products{left:141px;top:452px;width:639px;height:131px;border:1px solid var(--grey-line);border-radius:6px}
.links{position:absolute;list-style:none;color:var(--text-blue);font-size:13px;line-height:20.6px}
.links li{position:relative;padding-left:15px}
.links li::before{top:8px}
.seal{left:455px;top:8px}
.news-head{left:800px;top:449px;display:flex;align-items:center;gap:14px;color:var(--ink);font-size:20px}
.news-icon{width:35px;height:35px;border-radius:50%;border:2px solid #8aa6c3;background:#f2f5f9}
.news{left:804px;width:254px}
.news-item{border-bottom:1px solid var(--grey-line);padding-bottom:3px}
.news-item h3{font-size:13.5px;font-weight:400;color:var(--ink-dark);line-height:21px}
.news-item p{font-size:11.5px;color:var(--news-grey);line-height:20.6px;margin-top:6px}
.news-meta{display:flex;justify-content:space-between;font-size:11.5px;color:var(--ink-dark);padding:0 6px 0 3px;margin-top:2px}
.video{left:141px;top:614px;width:637px;height:284px;background:radial-gradient(ellipse at 50% 40%,#fbfbfb 0%,#e9e9e9 60%,#d2d2d2 100%)}
.play{position:absolute;left:270px;top:83px;width:72px;height:55px;background:#444;border-radius:2px}
.video h2{position:absolute;left:0;top:166px;width:100%;text-align:center;font-size:27px;line-height:37px;color:#444;font-weight:700}
.controls{position:absolute;left:0;bottom:0;width:100%;height:18px;background:#1f1f1f}
.footer{left:0;top:952px;width:1200px;height:226px;background:linear-gradient(100deg,#8fd0ec 0%,#45b1de 50%,#2aa3d6 100%)}
.company{left:377px;top:966px;color:#fff;font-size:14.5px;line-height:24.5px}
.social{display:flex;gap:9px;margin-top:9px}
.social span{width:24px;height:22px;background:#fff;border-radius:3px;opacity:.95}
.phones{color:#fff;font-size:17.5px;line-height:27px}
.footer-nav{left:0;top:1103px;width:1200px;height:40px;background:rgba(24,130,190,.45);border-top:1px solid rgba(255,255,255,.35);border-bottom:1px solid rgba(255,255,255,.35);display:flex;align-items:center;padding-left:126px;color:#fff;font-size:14.5px;font-weight:700}
.footer-nav span.sep,.legal span.sep{margin:0 20px;font-weight:400}
.legal{left:0;top:1143px;width:1200px;height:35px;background:#1f93cc;display:flex;align-items:center;justify-content:center;color:#fff;font-size:14px}
</style>
</head>
<body>
<div class="page">
  <header class="abs header">
    <div class="abs brand" style="left:136px;top:36px"><span class="brand-mark"></span><span>Humming<br>Desk</span></div>
    <p class="abs tagline">Be Confident your Phones are covered<span>what ever you are doing</span></p>
    <a class="abs login">
      <svg width="20" height="24" viewBox="0 0 20 24"><rect x="2" y="10" width="16" height="13" rx="2" fill="#3aa3da"/><path d="M5 10V7a5 5 0 0 1 10 0v3" fill="none" stroke="#3aa3da" stroke-width="2.5"/><rect x="9" y="14" width="2" height="5" fill="#fff"/></svg>Login</a>
  </header>

  <nav class="abs nav">
    <a class="active"><svg width="20" height="18" viewBox="0 0 20 18"><path d="M10 1 1 9h3v8h4v-5h4v5h4V9h3z" fill="#fff"/></svg>Home</a>
    <a>Phone Answering</a><a>Virtual Reception</a><a>FAQ</a><a>About Us</a>
  </nav>

  <div class="abs photo" role="img" aria-label="Photo of a smiling receptionist on the phone"></div>

  <ul class="abs features">
    <li>Live&nbsp; Phone Answering by Australian Virtual Receptionists</li>
    <li>Australian based professional receotionists will answer your phone<br>custamised to your requrements</li>
    <li>HD deliver excellent phone based business support solutions using smart</li>
    <li>Australian based team that cares about you, your business and clients</li>
    <li>Customizable inbound call management solutions aimed at the SME market</li>
    <li>Complete range of cost effective services to support any business</li>
  </ul>

  <section class="abs price">
    <p class="from">From as little as</p>
    <p class="amount">$4.90<small>per week</small></p>
    <div class="trial">Start a free trial</div>
    <div class="plans">Plans &amp; Pricing</div>
  </section>

  <section class="abs products">
    <ul class="links" style="left:26px;top:12px">
      <li>Product links</li><li>$1.90 per message</li><li>Value pack</li><li>Virtual Switchbord</li><li>Call over when not available</li>
    </ul>
    <ul class="links" style="left:231px;top:12px">
      <li>Complexs Services / Sales Scripts</li><li>Inbound</li><li>28 day prepay</li><li>Plans to suit higher users</li><li>Free 1300 Numbers</li>
    </ul>
    <svg class="abs seal" width="165" height="112" viewBox="0 0 165 112" role="img" aria-label="Refund policy seal"><circle cx="82" cy="54" r="52" fill="#35abd9"/></svg>
  </section>

  <div class="abs news-head"><span class="news-icon"></span>Latest news</div>
  <section class="abs news" style="top:497px">
    <article class="news-item">
      <h3>Lorem Ipsum is simply dummy text of the printing and typesetting industry.</h3>
      <p>Lorem Ipsum is simply dummy text of the printing and typesetting industry. Lorem Ipsum has been the industry's standard dummy</p>
      <div class="news-meta"><span>12 / 03 / 2012</span><span>Read more</span></div>
    </article>
    <article class="news-item" style="margin-top:3px">
      <h3>Lorem Ipsum is simply dummy text of the printing and typesetting industry.</h3>
      <p>Lorem Ipsum is simply dummy text of the printing and typesetting industry. Lorem Ipsum has been the industry's standard dummy</p>
      <div class="news-meta"><span>12 / 03 / 2012</span><span>Read more</span></div>
    </article>
    <article class="news-item" style="margin-top:4px;border:none">
      <h3>Lorem Ipsum is simply dummy text of the printing and typesetting industry.</h3>
      <p>Lorem Ipsum is simply dummy text of the printing and typesetting industry. Lorem Ipsum has been the industry's standard dummy</p>
      <div class="news-meta"><span>12 / 03 / 2012</span><span>Read more</span></div>
    </article>
  </section>

  <section class="abs video">
    <div class="play"><svg width="72" height="55" viewBox="0 0 72 55"><path d="M27 14v27l22-13.5z" fill="#fff"/></svg></div>
    <h2>Need Help Answering<br>Your Phones?</h2>
    <svg class="controls" viewBox="0 0 637 18">
      <path d="M11 5v8l7-4z" fill="#fff"/>
      <rect x="31" y="7" width="430" height="4" rx="2" fill="#555"/>
      <rect x="31" y="7" width="50" height="4" rx="2" fill="#bbb"/>
      <circle cx="83" cy="9" r="4.5" fill="#ddd"/>
      <text x="470" y="12" font-size="8" fill="#ccc" font-family="Arimo,sans-serif">1:30 · 4:23</text>
      <path d="M517 7h3l4-3v10l-4-3h-3z" fill="#ddd"/>
      <rect x="531" y="8" width="40" height="2" fill="#888"/>
      <circle cx="558" cy="9" r="4" fill="#ddd"/>
      <path d="M586 4h4M586 4v4M596 14h-4M596 14v-4M586 4l10 10" stroke="#ddd" stroke-width="1.4" fill="none"/>
      <circle cx="614" cy="9" r="4" fill="none" stroke="#ddd" stroke-width="2"/>
    </svg>
  </section>

  <footer class="abs footer"></footer>
  <div class="abs brand" style="left:138px;top:998px;font-size:24px;line-height:26px"><span class="brand-mark" style="width:40px;height:40px"></span><span>Humming<br>Desk</span></div>
  <div class="abs company">
    <p>Humming Desk Pty Ltd</p>
    <p>ABN: 51 824 753 556</p>
    <p>Suite 4, 12 Ocean St , Manly, NSW 2095</p>
    <p>info@hummingdesk.com.au</p>
    <div class="social"><span></span><span></span><span></span></div>
  </div>
  <svg class="abs" style="left:696px;top:968px" width="42" height="56" viewBox="0 0 42 56"><path d="M14 8c-6 2-8 10-6 20s8 18 14 19l5-7-6-5-3 2c-3-3-5-10-4-14l4-1-1-8z" fill="#fff"/><path d="M24 16a9 9 0 0 1 6 8M26 9a15 15 0 0 1 10 14" stroke="#fff" stroke-width="2.5" fill="none"/></svg>
  <div class="abs phones" style="left:748px;top:969px">+61 - 2 9000 1234</div>
  <div class="abs phones" style="left:915px;top:969px">+61 - 2 9000 1235</div>
  <div class="abs phones" style="left:748px;top:996px">+61 - 2 9000 1236</div>
  <div class="abs phones" style="left:915px;top:996px">+61 - 2 9000 1237</div>
  <div class="abs" style="left:716px;top:1032px;width:330px;height:1px;background:rgba(255,255,255,.5)"></div>
  <svg class="abs" style="left:708px;top:1038px" width="34" height="32" viewBox="0 0 34 32"><rect x="1" y="10" width="7" height="21" rx="2" fill="#fff"/><rect x="10" y="8" width="23" height="23" rx="2" fill="#fff"/><rect x="14" y="1" width="15" height="9" fill="none" stroke="#fff" stroke-width="2"/><g fill="#2ea6d8"><rect x="14" y="18" width="3" height="3"/><rect x="20" y="18" width="3" height="3"/><rect x="26" y="18" width="3" height="3"/><rect x="14" y="24" width="3" height="3"/><rect x="20" y="24" width="3" height="3"/><rect x="26" y="24" width="3" height="3"/></g></svg>
  <div class="abs phones" style="left:748px;top:1042px">+61 - 2 9000 1238</div>
  <div class="abs phones" style="left:919px;top:1042px">+61 - 2 9000 1239</div>

  <nav class="abs footer-nav">
    <span>Home</span><span class="sep">|</span><span>Phone Answering</span><span class="sep">|</span><span>Diary Management</span><span class="sep">|</span><span>Service Desk</span><span class="sep">|</span><span>Plans &amp; Pricing</span><span class="sep">|</span><span>FAQ</span><span class="sep">|</span><span>About Us</span><span class="sep">|</span><span>Free Trial</span>
  </nav>
  <div class="abs legal">
    <span>Copyright © 2011 Humming Desk Pty Ltd</span><span class="sep">|</span><span>Terms and conditions</span><span class="sep">|</span><span>Privacy</span><span class="sep">|</span><span>Contact</span>
  </div>
</div>
</body>
</html>
```